New Manager Resource Guide & Planner

I need a template designed for a resource guide and planner that new managers would use to help guide them their first year managing others. Think your typical planner injected with tips, worksheets, quotes and other helpful tools. Initially, I'd like a template created for some key pages: one month, one week and single day layouts plus a quote page. I'm attaching a very rudimentary idea of the project, just need it purposefully designed with my colors and branding. The size is 6" x 8 " h. I would like this done in InDesign or Keynote so I can edit it and create other pages. Most likely, though, will contract you to finish out the entire project.

Target Market(s)

new managers (and HR directors who will most likely purchase the resource planner for their employees)

Industry/Entity Type

Advertising

Font styles to use
Other font styles liked:
• archer, open sans

Requirements
Must have
• a creative feel to it (I come from the advertising industry, so a fun design is OK). use of my branding and colors, be noticeably well designed.
Nice to have
• look at other planners for ideas. my goal is to use your template to build out the other pages I need. So think cool edging, or stylized quote boxes, etc.
Should not have
• please use the colors in my palette in the attached pdf plus any other complementary colors you see fit. my branding uses the font archer, open sans, use these and any other fonts that you see fit.

```html
<!DOCTYPE html>
<html lang="en">
<head>
<meta charset="utf-8">
<title>New Manager Planner – Page Templates</title>
<link href="https://fonts.googleapis.com/css2?family=Jost:wght@400;500&family=Open+Sans:ital,wght@0,400;0,600;0,700;1,400&display=swap" rel="stylesheet">
<style>
  :root{
    --ink:#2b2b2b;
    --title:#3a1a2c;
    --lime:#e3e55f;
    --lime-strong:#c3cc35;
    --olive:#8a8a35;
    --rule:#555;
    --dot:#888;
    --paper:#ffffff;
  }
  html,body{margin:0;padding:0;overflow:hidden;background:#fff;}
  .sheet{position:relative;width:1200px;height:1200px;overflow:hidden;background:#fff;font-family:"Open Sans",sans-serif;color:var(--ink);}
  .page-title{position:absolute;width:365px;text-align:center;font-family:"Jost",sans-serif;font-weight:500;color:var(--title);font-size:33px;line-height:1;margin:0;}
  .page-title small{display:block;font-size:14px;font-weight:400;margin-top:-2px;}
  .page{position:absolute;width:365px;height:486px;background:var(--paper);box-shadow:0 0 18px rgba(90,90,140,.22);}
  .page svg{display:block;}
  .page text{font-family:"Open Sans",sans-serif;fill:var(--ink);}
  .dots{stroke:var(--dot);stroke-width:.8;stroke-dasharray:1.5 1.5;}
  .rule{stroke:var(--rule);stroke-width:1.5;}
  .lime{fill:var(--lime);}
  .lime-strong{fill:var(--lime-strong);}
  .olive{fill:var(--olive);}
  .grid line{stroke:var(--lime-strong);stroke-width:1.4;}
</style>
</head>
<body>
<main class="sheet">

  <h2 class="page-title" style="left:37px;top:46px;">Daily</h2>
  <h2 class="page-title" style="left:426px;top:46px;">Weekely</h2>
  <h2 class="page-title" style="left:815px;top:46px;">Daily<small>Optional</small></h2>
  <h2 class="page-title" style="left:37px;top:617px;">Monthly<small>Optional</small></h2>
  <h2 class="page-title" style="left:426px;top:617px;">Monthly</h2>
  <h2 class="page-title" style="left:815px;top:617px;">Quotes with note</h2>

  <!-- Daily page -->
  <section class="page daily" style="left:37px;top:113px;">
    <svg width="365" height="486" viewBox="0 0 456 608">
      <rect class="lime" x="8" y="8" width="227" height="100"/>
      <text x="121" y="56" font-size="19" font-weight="700" text-anchor="middle">19</text>
      <text x="26" y="100" font-size="13">Tuesday</text>
      <text x="177" y="100" font-size="13">March</text>
      <g font-size="12" font-style="italic" text-anchor="middle">
        <text x="346" y="34">Treat Employees like they</text>
        <text x="346" y="54">make a difference and they</text>
        <text x="346" y="74">will.</text>
      </g>
      <line class="rule" x1="8" y1="108" x2="449" y2="108"/>
      <text x="13" y="127" font-size="10.5" font-weight="700">Toda'y Schedule:</text>
      <text x="240" y="127" font-size="10.5" font-weight="700">To Do:</text>
      <g font-size="11.5">
        <text x="13" y="162">8:00</text><text x="13" y="186">9:00</text><text x="13" y="214">10:00</text>
        <text x="13" y="242">11:00</text><text x="13" y="270">12:00</text><text x="13" y="297">1:00</text>
        <text x="13" y="325">2:00</text><text x="13" y="353">3:00</text><text x="13" y="381">4:00</text>
        <text x="13" y="409">5:00</text><text x="13" y="437">6:00</text><text x="13" y="465">6:00</text>
        <text x="13" y="493">7:00</text><text x="13" y="515">8:00</text>
      </g>
      <g class="dots">
        <line x1="8" y1="168" x2="449" y2="168"/><line x1="8" y1="195" x2="449" y2="195"/>
        <line x1="8" y1="222" x2="449" y2="222"/><line x1="8" y1="250" x2="449" y2="250"/>
        <line x1="8" y1="277" x2="449" y2="277"/><line x1="8" y1="305" x2="449" y2="305"/>
        <line x1="8" y1="332" x2="449" y2="332"/><line x1="8" y1="360" x2="449" y2="360"/>
        <line x1="8" y1="387" x2="449" y2="387"/><line x1="8" y1="415" x2="449" y2="415"/>
        <line x1="8" y1="442" x2="449" y2="442"/><line x1="8" y1="470" x2="449" y2="470"/>
        <line x1="8" y1="497" x2="449" y2="497"/><line x1="8" y1="521" x2="449" y2="521"/>
      </g>
      <g fill="none" stroke="#333" stroke-width="1.2">
        <rect x="239" y="149" width="11" height="11"/><rect x="239" y="176" width="11" height="11"/>
        <rect x="239" y="204" width="11" height="11"/><rect x="239" y="231" width="11" height="11"/>
        <rect x="239" y="259" width="11" height="11"/><rect x="239" y="286" width="11" height="11"/>
        <rect x="239" y="314" width="11" height="11"/><rect x="239" y="341" width="11" height="11"/>
        <rect x="239" y="369" width="11" height="11"/><rect x="239" y="396" width="11" height="11"/>
        <rect x="239" y="424" width="11" height="11"/><rect x="239" y="451" width="11" height="11"/>
        <rect x="239" y="479" width="11" height="11"/><rect x="239" y="506" width="11" height="11"/>
      </g>
      <rect class="lime" x="8" y="525" width="223" height="76"/>
      <rect class="lime" x="238" y="525" width="211" height="76"/>
      <text x="13" y="539" font-size="10.5" font-weight="700">TONIGHT</text>
      <text x="242" y="540" font-size="10.5" font-weight="700">GRATITUDE</text>
    </svg>
  </section>

  <!-- Weekly page -->
  <section class="page weekly" style="left:426px;top:113px;">
    <svg width="365" height="486" viewBox="0 0 456 608">
      <text x="432" y="36" font-size="11.5" font-weight="700" text-anchor="end">March 2019</text>
      <line x1="8" y1="44" x2="449" y2="44" stroke="var(--olive)" stroke-width="3"/>
      <g font-size="13">
        <g transform="translate(0,68)">
          <circle class="olive" cx="34" cy="0" r="16"/><text x="34" y="5" text-anchor="middle" font-size="12" style="fill:#fff">18</text>
          <text x="57" y="4">Monday</text>
          <line class="dots" x1="17" y1="23" x2="449" y2="23"/><line class="dots" x1="17" y1="41" x2="449" y2="41"/><line class="dots" x1="17" y1="58" x2="449" y2="58"/>
          <line x1="17" y1="71" x2="449" y2="71" stroke="#999" stroke-width="1"/>
        </g>
        <g transform="translate(0,156)">
          <circle class="olive" cx="34" cy="0" r="16"/><text x="34" y="5" text-anchor="middle" font-size="12" style="fill:#fff">19</text>
          <text x="57" y="4">Tuesday</text>
          <line class="dots" x1="17" y1="23" x2="449" y2="23"/><line class="dots" x1="17" y1="41" x2="449" y2="41"/><line class="dots" x1="17" y1="58" x2="449" y2="58"/>
          <line x1="17" y1="71" x2="449" y2="71" stroke="#999" stroke-width="1"/>
        </g>
        <g transform="translate(0,245)">
          <circle class="olive" cx="34" cy="0" r="16"/><text x="34" y="5" text-anchor="middle" font-size="12" style="fill:#fff">20</text>
          <text x="57" y="4">Wednesday</text>
          <line class="dots" x1="17" y1="23" x2="449" y2="23"/><line class="dots" x1="17" y1="41" x2="449" y2="41"/><line class="dots" x1="17" y1="58" x2="449" y2="58"/>
          <line x1="17" y1="71" x2="449" y2="71" stroke="#999" stroke-width="1"/>
        </g>
        <g transform="translate(0,333)">
          <circle class="olive" cx="34" cy="0" r="16"/><text x="34" y="5" text-anchor="middle" font-size="12" style="fill:#fff">21</text>
          <text x="57" y="4">Thusday</text>
          <line class="dots" x1="17" y1="23" x2="449" y2="23"/><line class="dots" x1="17" y1="41" x2="449" y2="41"/><line class="dots" x1="17" y1="58" x2="449" y2="58"/>
          <line x1="17" y1="71" x2="449" y2="71" stroke="#999" stroke-width="1"/>
        </g>
        <g transform="translate(0,421)">
          <circle class="olive" cx="34" cy="0" r="16"/><text x="34" y="5" text-anchor="middle" font-size="12" style="fill:#fff">21</text>
          <text x="57" y="4">Friday</text>
          <line class="dots" x1="17" y1="23" x2="449" y2="23"/><line class="dots" x1="17" y1="41" x2="449" y2="41"/><line class="dots" x1="17" y1="58" x2="449" y2="58"/>
          <line x1="17" y1="71" x2="449" y2="71" stroke="#999" stroke-width="1"/>
        </g>
        <g transform="translate(0,510)">
          <circle class="olive" cx="34" cy="0" r="16"/><text x="34" y="5" text-anchor="middle" font-size="12" style="fill:#fff">22</text>
          <text x="57" y="4">Saturday</text>
          <line class="dots" x1="17" y1="31" x2="449" y2="31"/><line class="dots" x1="17" y1="48" x2="449" y2="48"/><line class="dots" x1="17" y1="64" x2="449" y2="64"/>
        </g>
      </g>
      <line x1="8" y1="592" x2="449" y2="592" stroke="var(--olive)" stroke-width="4"/>
    </svg>
  </section>

  <!-- Daily optional page -->
  <section class="page daily-optional" style="left:815px;top:113px;">
    <svg width="365" height="486" viewBox="0 0 456 608">
      <rect class="lime" x="8" y="8" width="222" height="100"/>
      <text x="121" y="56" font-size="19" font-weight="700" text-anchor="middle">19</text>
      <text x="26" y="100" font-size="13">Tuesday</text>
      <text x="177" y="100" font-size="13">March</text>
      <text x="241" y="23" font-size="12">Daily Goal</text>
      <line class="rule" x1="8" y1="108" x2="449" y2="108"/>
      <line class="rule" x1="230" y1="108" x2="230" y2="608"/>
      <text x="13" y="127" font-size="10.5" font-weight="700">Toda'y Schedule:</text>
      <text x="240" y="127" font-size="10.5" font-weight="700">Sales Activity:</text>
      <g font-size="11.5">
        <text x="13" y="162">8:00</text><text x="13" y="186">9:00</text><text x="13" y="214">10:00</text>
        <text x="13" y="242">11:00</text><text x="13" y="270">12:00</text><text x="13" y="297">1:00</text>
        <text x="13" y="325">2:00</text><text x="13" y="353">3:00</text><text x="13" y="381">4:00</text>
        <text x="13" y="409">5:00</text><text x="13" y="437">6:00</text><text x="13" y="465">6:00</text>
        <text x="13" y="493">7:00</text><text x="13" y="515">8:00</text>
      </g>
      <g class="dots">
        <line x1="8" y1="168" x2="226" y2="168"/><line x1="8" y1="195" x2="226" y2="195"/>
        <line x1="8" y1="222" x2="226" y2="222"/><line x1="8" y1="250" x2="226" y2="250"/>
        <line x1="8" y1="277" x2="226" y2="277"/><line x1="8" y1="305" x2="226" y2="305"/>
        <line x1="8" y1="332" x2="226" y2="332"/><line x1="8" y1="360" x2="226" y2="360"/>
        <line x1="8" y1="387" x2="226" y2="387"/><line x1="8" y1="415" x2="226" y2="415"/>
        <line x1="8" y1="442" x2="226" y2="442"/><line x1="8" y1="470" x2="226" y2="470"/>
        <line x1="8" y1="497" x2="226" y2="497"/><line x1="8" y1="521" x2="226" y2="521"/>
      </g>
      <g fill="none" stroke="#333" stroke-width="1.2">
        <circle cx="241" cy="149" r="5"/><circle cx="241" cy="168" r="5"/><circle cx="241" cy="188" r="5"/>
        <circle cx="241" cy="207" r="5"/><circle cx="241" cy="227" r="5"/><circle cx="241" cy="246" r="5"/>
        <circle cx="241" cy="266" r="5"/><circle cx="241" cy="285" r="5"/><circle cx="241" cy="305" r="5"/>
        <circle cx="241" cy="324" r="5"/><circle cx="241" cy="344" r="5"/><circle cx="241" cy="363" r="5"/>
        <circle cx="241" cy="383" r="5"/><circle cx="241" cy="402" r="5"/>
      </g>
      <g class="dots">
        <line x1="250" y1="159" x2="449" y2="159"/><line x1="250" y1="179" x2="449" y2="179"/>
        <line x1="250" y1="198" x2="449" y2="198"/><line x1="250" y1="218" x2="449" y2="218"/>
        <line x1="250" y1="237" x2="449" y2="237"/><line x1="250" y1="257" x2="449" y2="257"/>
        <line x1="250" y1="276" x2="449" y2="276"/><line x1="250" y1="296" x2="449" y2="296"/>
        <line x1="250" y1="315" x2="449" y2="315"/><line x1="250" y1="335" x2="449" y2="335"/>
        <line x1="250" y1="354" x2="449" y2="354"/><line x1="250" y1="374" x2="449" y2="374"/>
        <line x1="250" y1="393" x2="449" y2="393"/><line x1="250" y1="412" x2="449" y2="412"/>
      </g>
      <line class="rule" x1="230" y1="419" x2="449" y2="419"/>
      <text x="235" y="434" font-size="11">Notes</text>
      <g class="dots">
        <line x1="252" y1="442" x2="252" y2="602"/>
        <line x1="235" y1="448" x2="449" y2="448"/><line x1="235" y1="466" x2="449" y2="466"/>
        <line x1="235" y1="484" x2="449" y2="484"/><line x1="235" y1="502" x2="449" y2="502"/>
        <line x1="235" y1="520" x2="449" y2="520"/><line x1="235" y1="538" x2="449" y2="538"/>
        <line x1="235" y1="556" x2="449" y2="556"/><line x1="235" y1="574" x2="449" y2="574"/>
        <line x1="235" y1="592" x2="449" y2="592"/>
      </g>
      <rect class="lime" x="8" y="525" width="218" height="76"/>
      <text x="13" y="539" font-size="10.5" font-weight="700">TONIGHT</text>
    </svg>
  </section>

  <!-- Month at a glance -->
  <section class="page month-glance" style="left:37px;top:674px;">
    <svg width="365" height="486" viewBox="0 0 456 608">
      <rect class="lime-strong" x="8" y="8" width="441" height="39"/>
      <text x="14" y="36" font-size="21" font-weight="700" style="fill:#2a2a1a">MONTH AT A GLANCE</text>
      <text x="440" y="32" font-size="13" text-anchor="end" style="fill:#444">March</text>
      <rect class="lime" x="8" y="47" width="441" height="29"/>
      <g font-size="12.5" font-weight="700" text-anchor="middle">
        <text x="42" y="67">Mon</text><text x="106" y="67">Tue</text><text x="163" y="67">Wed</text>
        <text x="227" y="67">Thu</text><text x="291" y="67">Fri</text><text x="353" y="67">Sat</text><text x="414" y="67">Sun</text>
      </g>
      <g class="grid">
        <line x1="74" y1="47" x2="74" y2="76" stroke="#fff"/>
        <line x1="12" y1="76" x2="12" y2="502"/><line x1="74" y1="76" x2="74" y2="502"/>
        <line x1="136" y1="76" x2="136" y2="502"/><line x1="198" y1="76" x2="198" y2="502"/>
        <line x1="260" y1="76" x2="260" y2="502"/><line x1="322" y1="76" x2="322" y2="502"/>
        <line x1="384" y1="76" x2="384" y2="502"/><line x1="445" y1="76" x2="445" y2="502"/>
        <line x1="12" y1="76" x2="445" y2="76"/><line x1="12" y1="147" x2="445" y2="147"/>
        <line x1="12" y1="218" x2="445" y2="218"/><line x1="12" y1="289" x2="445" y2="289"/>
        <line x1="12" y1="360" x2="445" y2="360"/><line x1="12" y1="431" x2="445" y2="431"/>
        <line x1="12" y1="502" x2="445" y2="502"/>
      </g>
      <g stroke="#fff" stroke-width="1.4">
        <line x1="74" y1="47" x2="74" y2="76"/><line x1="136" y1="47" x2="136" y2="76"/>
        <line x1="198" y1="47" x2="198" y2="76"/><line x1="260" y1="47" x2="260" y2="76"/>
        <line x1="322" y1="47" x2="322" y2="76"/><line x1="384" y1="47" x2="384" y2="76"/>
      </g>
      <text x="16" y="527" font-size="12.5" font-weight="700">Notes</text>
      <g stroke="#333" stroke-width="1.2">
        <line x1="74" y1="529" x2="440" y2="529"/>
        <line x1="16" y1="555" x2="440" y2="555"/>
        <line x1="16" y1="581" x2="440" y2="581"/>
      </g>
    </svg>
  </section>

  <!-- Monthly planner -->
  <section class="page month-planner" style="left:426px;top:674px;">
    <svg width="365" height="486" viewBox="0 0 456 608">
      <text x="10" y="20" font-size="11.5" font-weight="700">March 2019</text>
      <rect x="8" y="25" width="441" height="4" fill="#111"/>
      <rect class="lime" x="8" y="29" width="221" height="64"/>
      <text x="10" y="39" font-size="8">Big Picture</text>
      <g class="dots"><line x1="10" y1="48" x2="210" y2="48"/><line x1="10" y1="63" x2="210" y2="63"/><line x1="10" y1="78" x2="210" y2="78"/></g>
      <g font-size="4" text-anchor="middle" font-weight="700">
        <text x="290" y="36">Prev Month</text>
        <text x="392" y="36">Next Month</text>
      </g>
      <g stroke="#bbb" stroke-width=".6" fill="none">
        <rect x="248" y="39" width="84" height="50"/>
        <line x1="248" y1="46" x2="332" y2="46"/><line x1="248" y1="53" x2="332" y2="53"/><line x1="248" y1="60" x2="332" y2="60"/>
        <line x1="248" y1="67" x2="332" y2="67"/><line x1="248" y1="74" x2="332" y2="74"/><line x1="248" y1="81" x2="332" y2="81"/>
        <line x1="260" y1="39" x2="260" y2="89"/><line x1="272" y1="39" x2="272" y2="89"/><line x1="284" y1="39" x2="284" y2="89"/>
        <line x1="296" y1="39" x2="296" y2="89"/><line x1="308" y1="39" x2="308" y2="89"/><line x1="320" y1="39" x2="320" y2="89"/>
        <rect x="350" y="39" width="84" height="50"/>
        <line x1="350" y1="46" x2="434" y2="46"/><line x1="350" y1="53" x2="434" y2="53"/><line x1="350" y1="60" x2="434" y2="60"/>
        <line x1="350" y1="67" x2="434" y2="67"/><line x1="350" y1="74" x2="434" y2="74"/><line x1="350" y1="81" x2="434" y2="81"/>
        <line x1="362" y1="39" x2="362" y2="89"/><line x1="374" y1="39" x2="374" y2="89"/><line x1="386" y1="39" x2="386" y2="89"/>
        <line x1="398" y1="39" x2="398" y2="89"/><line x1="410" y1="39" x2="410" y2="89"/><line x1="422" y1="39" x2="422" y2="89"/>
      </g>
      <line class="rule" x1="233" y1="29" x2="233" y2="608"/>
      <line class="rule" x1="233" y1="96" x2="449" y2="96"/>
      <line x1="8" y1="96" x2="229" y2="96" stroke="#999" stroke-width="1"/>
      <text x="10" y="110" font-size="8">To Do:</text>
      <g class="dots">
        <line x1="24" y1="116" x2="24" y2="600"/>
        <line x1="8" y1="120" x2="222" y2="120"/><line x1="8" y1="138" x2="222" y2="138"/><line x1="8" y1="155" x2="222" y2="155"/>
        <line x1="8" y1="173" x2="222" y2="173"/><line x1="8" y1="190" x2="222" y2="190"/><line x1="8" y1="208" x2="222" y2="208"/>
        <line x1="8" y1="225" x2="222" y2="225"/><line x1="8" y1="243" x2="222" y2="243"/><line x1="8" y1="260" x2="222" y2="260"/>
        <line x1="8" y1="278" x2="222" y2="278"/><line x1="8" y1="295" x2="222" y2="295"/><line x1="8" y1="313" x2="222" y2="313"/>
        <line x1="8" y1="330" x2="222" y2="330"/><line x1="8" y1="348" x2="222" y2="348"/><line x1="8" y1="365" x2="222" y2="365"/>
        <line x1="8" y1="383" x2="222" y2="383"/><line x1="8" y1="400" x2="222" y2="400"/><line x1="8" y1="418" x2="222" y2="418"/>
        <line x1="8" y1="435" x2="222" y2="435"/><line x1="8" y1="453" x2="222" y2="453"/><line x1="8" y1="470" x2="222" y2="470"/>
        <line x1="8" y1="488" x2="222" y2="488"/><line x1="8" y1="505" x2="222" y2="505"/><line x1="8" y1="523" x2="222" y2="523"/>
        <line x1="8" y1="540" x2="222" y2="540"/><line x1="8" y1="558" x2="222" y2="558"/><line x1="8" y1="575" x2="222" y2="575"/>
        <line x1="8" y1="593" x2="222" y2="593"/>
      </g>
      <g font-size="8">
        <text x="238" y="112">Deadlines</text>
        <text x="238" y="247">Financial</text>
        <text x="238" y="386">Project</text>
        <text x="238" y="523">Other</text>
      </g>
      <g class="rule"><line x1="233" y1="232" x2="449" y2="232"/><line x1="233" y1="371" x2="449" y2="371"/><line x1="233" y1="508" x2="449" y2="508"/></g>
      <g class="dots">
        <line x1="237" y1="120" x2="449" y2="120"/><line x1="237" y1="138" x2="449" y2="138"/><line x1="237" y1="155" x2="449" y2="155"/>
        <line x1="237" y1="173" x2="449" y2="173"/><line x1="237" y1="190" x2="449" y2="190"/><line x1="237" y1="208" x2="449" y2="208"/>
        <line x1="237" y1="225" x2="449" y2="225"/>
        <line x1="237" y1="260" x2="449" y2="260"/><line x1="237" y1="278" x2="449" y2="278"/><line x1="237" y1="295" x2="449" y2="295"/>
        <line x1="237" y1="313" x2="449" y2="313"/><line x1="237" y1="330" x2="449" y2="330"/><line x1="237" y1="348" x2="449" y2="348"/>
        <line x1="237" y1="364" x2="449" y2="364"/>
        <line x1="237" y1="400" x2="449" y2="400"/><line x1="237" y1="418" x2="449" y2="418"/><line x1="237" y1="435" x2="449" y2="435"/>
        <line x1="237" y1="453" x2="449" y2="453"/><line x1="237" y1="470" x2="449" y2="470"/><line x1="237" y1="488" x2="449" y2="488"/>
        <line x1="237" y1="537" x2="449" y2="537"/><line x1="237" y1="555" x2="449" y2="555"/><line x1="237" y1="572" x2="449" y2="572"/>
        <line x1="237" y1="590" x2="449" y2="590"/>
      </g>
    </svg>
  </section>

  <!-- Quote page -->
  <section class="page quote" style="left:815px;top:674px;">
    <svg width="365" height="486" viewBox="0 0 456 608">
      <circle class="lime" cx="231" cy="176" r="168"/>
      <g font-size="23" font-weight="700" text-anchor="middle" style="fill:#1e1e14">
        <text x="231" y="148">Treat Employees like</text>
        <text x="231" y="187">they make a difference</text>
        <text x="231" y="226">and they will.</text>
      </g>
      <g class="dots">
        <line x1="46" y1="400" x2="398" y2="400"/><line x1="46" y1="416" x2="398" y2="416"/>
        <line x1="46" y1="432" x2="398" y2="432"/><line x1="46" y1="448" x2="398" y2="448"/>
        <line x1="46" y1="464" x2="398" y2="464"/><line x1="46" y1="480" x2="398" y2="480"/>
      </g>
      <rect class="olive" x="8" y="517" width="441" height="84" stroke="#c3cc35" stroke-width="1.5"/>
    </svg>
  </section>

</main>
</body>
</html>
```